Business Card / Appointment Card for Physician

On one side it should give the logo, address, and contact information, and on the other side it should br an Appointment card.

One Side:
Logo (see attached files)
Board Certified American Orthopedic Surgery

1487 Harrowgate Ave.
Suite KM7
Bronx, NY 10527
Tel: (718) 552 - 1948
Fax: (718) 552 - 7210

628 Fourth Ave.
Suite 42
New York, NY 10087
Tel: (212) 734 - 2815

Second Side:
Appointment
give them a choice of Bronx or Mahattan office
For:
Date:
Time:

If you are unable to keep your appointment, please call (718) 263-5102 24hrs in advance.

Target Market(s)

People that need orthopedic surgery

Industry/Entity Type

Business

Contact Information for Business Card

smart and attractive

Requirements
Must have
• logo
• contact information on one side, appointment information on the other

```html
<!DOCTYPE html>
<html lang="en">
<head>
<meta charset="utf-8">
<title>Daniel R. Haverford MD PC – Business &amp; Appointment Card</title>
<link rel="stylesheet" href="https://fonts.googleapis.com/css2?family=PT+Sans:ital,wght@0,400;0,700;1,400&family=PT+Sans+Narrow:wght@700&family=Questrial&display=swap">
<style>
  :root {
    --brand-blue: #0b66ad;
    --brand-green: #6db33f;
    --ink: #1d1d1b;
    --paper: #ffffff;
    --paper-soft: #f3f5f6;
    --stage: #e9e6e3;
  }
  * { box-sizing: border-box; margin: 0; padding: 0; }
  html, body {
    width: 1200px; height: 900px; overflow: hidden;
    background: var(--stage);
  }
  .canvas { position: relative; width: 1200px; height: 900px; }

  /* ---------- Business card ---------- */
  .business-card {
    position: absolute; left: 78px; top: 35px;
    width: 587px; height: 363px;
    background: var(--paper);
    overflow: hidden;
    font-family: "PT Sans", sans-serif;
  }
  .business-card .card-shapes { position: absolute; inset: 0; }
  .brand {
    position: absolute; left: 0; right: 0; top: 22px;
    text-align: center; color: var(--brand-blue);
  }
  .brand-mark {
    display: block; width: 68px; height: 68px; margin: 0 auto 10px;
    border-radius: 50%; background: var(--brand-blue);
  }
  .brand-name {
    font-family: "Questrial", sans-serif;
    font-size: 23px; letter-spacing: 0.3px; line-height: 1;
  }
  .brand-specialty {
    font-family: "Questrial", sans-serif;
    font-size: 12.5px; margin-top: 3px; letter-spacing: 0.2px;
  }
  .certification {
    position: absolute; left: 0; right: 0; top: 151px;
    text-align: center; color: var(--ink);
    font-family: "PT Sans Narrow", sans-serif; font-weight: 700; font-size: 16px;
  }
  .office {
    position: absolute; color: var(--paper);
    font-size: 16px; line-height: 21px;
  }
  .office-manhattan { left: 35px; top: 244px; }
  .office-bronx { right: 35px; top: 231px; text-align: right; }
  .phone-line { display: flex; align-items: center; gap: 4px; margin-top: 2px; }
  .office-bronx .phone-line { justify-content: flex-end; }
  .icon { width: 17px; height: 17px; flex: none; }

  /* ---------- Appointment card ---------- */
  .appointment-card {
    position: absolute; left: 388px; top: 505px;
    width: 567px; height: 352px;
    background: var(--paper-soft);
    overflow: hidden;
    font-family: "PT Sans", sans-serif; color: var(--ink);
  }
  .appointment-card .card-shapes { position: absolute; inset: 0; }
  .appointment-title {
    position: absolute; left: 0; right: 0; top: 24px;
    text-align: center; color: var(--paper);
    font-weight: 700; font-size: 26px; letter-spacing: 0.3px;
  }
  .office-choice {
    position: absolute; top: 104px;
    display: flex; align-items: center; gap: 7px; font-size: 19px;
  }
  .office-choice.bronx { left: 62px; }
  .office-choice.manhattan { left: 348px; }
  .checkbox {
    width: 14px; height: 14px; border: 1.6px solid var(--ink); background: var(--paper-soft);
  }
  .field {
    position: absolute; left: 60px; width: 450px;
    display: flex; align-items: flex-end; font-size: 19px; font-weight: 700;
  }
  .field .rule { flex: 1; border-bottom: 1.3px solid var(--ink); margin-bottom: 6px; margin-left: 2px; }
  .field-for { top: 155px; }
  .field-for .rule { margin-left: 12px; }
  .field-date { top: 203px; }
  .field-time { top: 251px; }
  .cancellation-note {
    position: absolute; left: 0; right: 0; bottom: 18px;
    text-align: center; color: var(--paper);
    font-style: italic; font-size: 13px;
  }
</style>
</head>
<body>
<main class="canvas">

  <section class="business-card" aria-label="Business card">
    <svg class="card-shapes" width="587" height="363" viewBox="0 0 587 363" aria-hidden="true">
      <polygon points="0,199 333,199 314,222 0,222" fill="var(--brand-green)"/>
      <polygon points="0,226 326,226 351,191 587,191 587,363 0,363" fill="var(--brand-blue)"/>
    </svg>

    <header class="brand">
      <span class="brand-mark" aria-hidden="true"></span>
      <div class="brand-name">DANIEL R. HAVERFORD MD PC</div>
      <div class="brand-specialty">ORTHOPAEDIC SURGERY &amp; SPORTS MEDICINE</div>
    </header>
    <p class="certification">Board Certified American Orthopedic Surgery</p>

    <address class="office office-manhattan" style="font-style:normal">
      628 Fourth Ave.<br>
      Suite 42<br>
      New York, NY 10087
      <span class="phone-line" style="margin-top:8px">
        <svg class="icon" viewBox="0 0 20 20" aria-label="Telephone"><circle cx="10" cy="10" r="10" fill="#fff"/><path d="M6.4 4.8l2 2.2-1 1.6c.7 1.6 2 2.9 3.6 3.6l1.6-1 2.2 2-1.2 1.9c-4.1-.4-8-4.3-8.4-8.4z" fill="var(--brand-blue)"/></svg>
        (212) 734 - 2815
      </span>
    </address>

    <address class="office office-bronx" style="font-style:normal">
      1487 Harrowgate Ave.<br>
      Suite KM7<br>
      Bronx, NY 10527
      <span class="phone-line" style="margin-top:6px">
        (718) 552 - 1948
        <svg class="icon" viewBox="0 0 20 20" aria-label="Telephone"><circle cx="10" cy="10" r="10" fill="#fff"/><path d="M6.4 4.8l2 2.2-1 1.6c.7 1.6 2 2.9 3.6 3.6l1.6-1 2.2 2-1.2 1.9c-4.1-.4-8-4.3-8.4-8.4z" fill="var(--brand-blue)"/></svg>
      </span>
      <span class="phone-line">
        (718) 552 - 7210
        <svg class="icon" viewBox="0 0 20 20" aria-label="Fax"><circle cx="10" cy="10" r="10" fill="#fff"/><rect x="6" y="4.5" width="8" height="4" fill="none" stroke="var(--brand-blue)" stroke-width="1.3"/><rect x="5" y="8.5" width="10" height="7" rx="1" fill="var(--brand-blue)"/><rect x="7" y="10.5" width="6" height="1.2" fill="#fff"/></svg>
      </span>
    </address>
  </section>

  <section class="appointment-card" aria-label="Appointment card">
    <svg class="card-shapes" width="567" height="352" viewBox="0 0 567 352" aria-hidden="true">
      <path d="M0 0H567V66Q283 56 0 84Z" fill="var(--brand-green)"/>
      <path d="M0 295Q283 285 567 298V352H0Z" fill="var(--brand-blue)"/>
    </svg>

    <h1 class="appointment-title">APPOINTMENT</h1>

    <label class="office-choice bronx"><span class="checkbox"></span>Bronx Office</label>
    <label class="office-choice manhattan"><span class="checkbox"></span>Mahattan office</label>

    <div class="field field-for"><span>For:</span><span class="rule"></span></div>
    <div class="field field-date"><span>Date:</span><span class="rule"></span></div>
    <div class="field field-time"><span>Time:</span><span class="rule"></span></div>

    <p class="cancellation-note">If you are unable to keep your appointment,please call (718) 263-5102 24hrs in advance.</p>
  </section>

</main>
</body>
</html>
```